SEO and image area for top of invitation website

We need to add an area on our final category pages for SEO text. Instead of just adding text, we'd like to develop a graphical approach that keeps with our soft, feminine look.

You can view an example of our current final category page at http://www.cardmeadow.example/invitations/boy-birthday

I've attached an image of what we're thinking it could look like, but you're welcome to alter the design.

The area should be the same width as our site, but can be any height you determine appropriate.

The winner of this project may be approached to develop the additional designs and backgrounds for us as another project. We additionally have several other projects we're interested in doing with the winner.
Updates

We have had a question about the right side of the banner, and what "Free Unlimited Proofs" mean.

About Free Unlimited Proofs:

We are a custom invitation printing company. When a customer orders an invitation from us, they tell us what information we want on the invitation. We then create an electronic sample, or "proof", of what it will look like. We then email it to the customer and they can tell us if they want to make any more changes. We will continue to send them samples, or what we call "proofs", until they are completely satisfied with the way it looks.

We offer Free UNLIMITED Proofs. Compared to our competitors, we are the only one to offer free unlimited proofs.

So, for the right side of this banner, we need an image, or a badge, promoting that we offer free unlimited proofs, and you can include that we are the only ones to do it, if your design has space for that information.

Also, keep in mind, that for other category pages, we may create different images or badges to put in this area - such as for our Low Price Guarantee or to promote a coupon or specific product, for example. So, your design should be able to work with various images on the right side.

Target Market(s)

Our demographic is 100% women, ages 25-60.

Industry/Entity Type

Seo

Requirements
Must have
• The area must have 3 things:
1) Area for the title of the page.
2) Area for SEO text describing the category page.
3) Area for an image. Keep in mind that this image may change for each category page. For this project, you will create an image for our offering of "Free Unlimited Proofs". On other pages, we may display other images we create such as "Low Price Guarantee" or images of certain products we'd like to promote. Just keep this in mind when you're making the design flow.
Nice to have
• Optional: Light design background. We wouldn't mind there being a slight graphical background to this area, to keep it interesting to the eye. Then, for other category pages, we may make additional backgrounds to use in this box area.

```html
<!DOCTYPE html>
<html lang="en">
<head>
<meta charset="utf-8">
<title>Card Meadow – Boy Birthday Invitations</title>
<link rel="stylesheet" href="https://fonts.googleapis.com/css2?family=Noto+Serif:wght@400;700&family=Open+Sans:wght@400;600;700&family=Roboto:wght@400;700&display=swap">
<style>
:root{
  --ink:#5e5557;
  --text:#666;
  --line:#d8d8d8;
  --teal:#1a9e9e;
  --teal-btn:#4fc1b8;
  --bar:#f4f4f4;
  --tile:#efefef;
  --btn-top:#ffe78a;
  --btn-bot:#f6c430;
  --headline:#ffef1a;
  --badge:#d9608a;
  --badge-ring:#fff3f7;
}
*{box-sizing:border-box;margin:0;padding:0}
html,body{width:1200px;height:960px;overflow:hidden;background:#fff}
body{position:relative;font-family:"Open Sans",sans-serif;color:var(--text)}
.abs{position:absolute}

.utility-bar{left:0;top:0;width:1200px;height:28px;background:var(--bar);border-bottom:1px solid #e2e2e2;
  display:flex;justify-content:center;align-items:center;font-size:12px;font-weight:600;color:#555}
.utility-bar .item{display:flex;align-items:center;gap:7px;padding:0 12px;height:28px;border-right:1px solid #ddd}
.utility-bar .item:last-child{border-right:none}
.utility-bar svg{fill:#666}

.brand{left:146px;top:44px;display:flex;align-items:center;gap:12px}
.brand .mark{width:56px;height:56px;background:#efe9ea;border:1px solid #ddd;box-shadow:0 2px 3px rgba(0,0,0,.15)}
.brand .name{font-family:"Noto Serif",serif;font-size:35px;color:var(--ink);letter-spacing:-.5px}

.search{left:486px;top:63px;width:276px;height:44px;border:3px solid #f0f0f0;border-radius:6px;background:#fff}
.search .btn{position:absolute;right:6px;top:6px;width:62px;height:26px;background:#c9c9c9;border-radius:3px;
  color:#fff;font-family:"Noto Serif",serif;font-weight:700;font-size:12px;text-align:center;line-height:26px}
.account{left:783px;top:76px;display:flex;align-items:center;gap:15px;font-family:"Noto Serif",serif;font-size:12px;color:#555}
.account .count{font-size:16px;color:#777;margin-left:-8px}

.main-nav{left:143px;top:134px;width:914px;height:44px;border-top:1px solid var(--line);border-bottom:1px solid var(--line);
  display:flex;align-items:center;gap:38px;padding-left:20px;font-family:"Noto Serif",serif;font-size:18px;color:var(--text)}

.breadcrumb{left:144px;top:197px;font-family:"Noto Serif",serif;font-size:12px;color:#666}
.breadcrumb a{color:var(--teal);text-decoration:none}

.hero{left:141px;top:248px;width:664px;height:170px;overflow:hidden}
.hero .photo{position:absolute;left:0;top:0;width:664px;height:170px;
  background:linear-gradient(90deg,#e9cdb9 0%,#f1ddd0 20%,#a9c6e6 32%,#f0e7a0 45%,#c8b5e6 58%,#f2c5cf 72%,#cfe4a5 86%,#f5d8a0 100%)}
.hero .title{position:absolute;left:330px;top:10px;width:334px;text-align:center;font-family:"Noto Serif",serif;font-weight:700;
  color:var(--headline);text-shadow:-1px -1px 0 #3a2f20,1px -1px 0 #3a2f20,-1px 1px 0 #3a2f20,1px 1px 0 #3a2f20;line-height:1}
.hero .title .l1{display:block;font-size:37px}
.hero .title .l2{display:block;font-size:25px;margin-top:4px}
.hero .tag{position:absolute;left:330px;top:79px;width:334px;text-align:center;font-family:"Roboto",sans-serif;font-size:17px;color:#111}
.hero .seo{position:absolute;left:340px;top:106px;width:314px;padding:5px 8px;background:rgba(255,255,255,.72);border-radius:6px;
  font-size:10.5px;line-height:14px;color:#555;text-align:center}

.side-photo{left:822px;top:248px;width:248px;height:170px;
  background:linear-gradient(135deg,#6b7a3e 0%,#a98a66 35%,#e3c2a4 55%,#58703a 100%)}
.proof-badge{left:948px;top:284px;width:112px;height:112px;border-radius:50%;background:var(--badge);
  border:4px solid var(--badge-ring);box-shadow:0 2px 6px rgba(0,0,0,.25);
  display:flex;flex-direction:column;align-items:center;justify-content:center;text-align:center;color:#fff;font-family:"Roboto",sans-serif}
.proof-badge .big{font-size:14px;font-weight:700;line-height:16px;text-transform:uppercase}
.proof-badge .small{font-size:9.5px;line-height:12px;margin-top:4px}

.sort{left:158px;top:429px;display:flex;align-items:baseline;gap:18px;font-family:"Noto Serif",serif;font-size:12px;color:#555}
.sort .label{font-size:16px;color:#666}
.pager{left:867px;top:435px;display:flex;align-items:center;gap:7px;font-family:"Noto Serif",serif;font-size:13px;color:var(--teal)}
.pager .n:first-of-type{color:#555}
.pager .arrow{width:20px;height:20px;border-radius:50%;display:flex;align-items:center;justify-content:center}
.pager .prev{background:#ccc}.pager .next{background:var(--teal-btn)}

.filters{left:144px;top:484px;width:229px}
.filter-head{display:flex;align-items:center;gap:9px;font-family:"Noto Serif",serif;font-size:16px;color:#666;padding-left:9px}
.colors{list-style:none;margin:10px 0 0 25px;font-size:12px;color:#777}
.colors li{display:flex;align-items:center;gap:7px;height:18.8px}
.colors .dot{width:14px;height:14px;border-radius:50%;border:1px solid #aaa}
.colors .all{margin-left:4px;text-transform:uppercase;color:#666}
.filter-block{border-top:3px solid #d6d6d6;height:59px;padding-top:13px}

.tile{width:222px;height:208px;background:var(--tile);border:1px solid #d7d7d7}
.tile .art{position:absolute}
.quick{position:absolute;bottom:-10px;left:50%;transform:translateX(-50%);width:94px;height:25px;border-radius:5px;
  background:linear-gradient(var(--btn-top),var(--btn-bot));border:1px solid #e0b22c;font-size:11px;font-weight:700;color:#5a4a20;
  text-align:center;line-height:23px;box-shadow:0 1px 2px rgba(0,0,0,.2)}
</style>
</head>
<body>

<header class="utility-bar abs">
  <div class="item">
    <svg width="16" height="12" viewBox="0 0 16 12"><rect x="0" y="1" width="10" height="8"/><path d="M10 4h3l3 3v2h-6z"/><circle cx="3" cy="10.5" r="1.5"/><circle cx="12.5" cy="10.5" r="1.5"/></svg>
    FREE SHIPPING on orders over $150 - no coupon needed!
  </div>
  <div class="item">
    <svg width="16" height="13" viewBox="0 0 16 13"><path d="M1 1h10v7H5l-3 3V8H1z"/><path d="M12 4h3v6h-1v2l-2-2H7V9h5z"/></svg>
    Live Help
  </div>
  <div class="item">
    <svg width="16" height="12" viewBox="0 0 16 12"><path d="M1 3c0-2 14-2 14 0v2h-4V3H5v2H1z"/><rect x="3" y="6" width="10" height="5" rx="1"/></svg>
    555.010.2468
  </div>
  <div class="item">
    <svg width="14" height="14" viewBox="0 0 14 14"><path d="M1 1h6l6 6-6 6-6-6z"/><circle cx="4" cy="4" r="1.3" fill="#f4f4f4"/></svg>
    Become a Designer · Earn Commission
  </div>
</header>

<div class="brand abs"><div class="mark"></div><div class="name">Card Meadow</div></div>
<div class="search abs"><div class="btn">search</div></div>
<div class="account abs">
  <span>LOGIN</span><span>CREATE ACCOUNT</span>
  <svg width="20" height="16" viewBox="0 0 20 16" fill="#777"><path d="M0 1h4l3 9h10l2-7H6" fill="none" stroke="#777" stroke-width="2"/><circle cx="8" cy="14" r="1.6"/><circle cx="16" cy="14" r="1.6"/></svg>
  <span class="count">0</span>
</div>

<nav class="main-nav abs">
  <span>Wedding</span><span>Party</span><span>Baby and Kids</span><span>Holiday</span><span>Graduation</span><span>Business</span><span>Stationery</span>
</nav>

<div class="breadcrumb abs"><a>Party</a> · <a>Kids Birthday Party Invitations</a> · Boy Birthday Invitations</div>

<section class="hero abs">
  <div class="photo" role="img" aria-label="Photo of a mother and baby with a birthday cupcake beside colourful party balloons"></div>
  <h1 class="title"><span class="l1">A Very Special</span><span class="l2">Birthday Invitations</span></h1>
  <p class="tag">Low Price Guarantee</p>
  <p class="seo">Celebrate your little guy with boy birthday invitations for every theme, from pirates and dinosaurs to bowling and outer space, each personalized just for him.</p>
</section>
<div class="side-photo abs" role="img" aria-label="Photo of two young girls blowing out candles on a birthday cake"></div>
<div class="proof-badge abs">
  <span class="big">Free<br>Unlimited<br>Proofs</span>
  <span class="small">the only ones<br>who offer it</span>
</div>

<div class="sort abs"><span class="label">Sort By:</span><span>Price</span><span>Name</span><span>Vendor</span></div>
<div class="pager abs">
  <span class="arrow prev"><svg width="10" height="10" viewBox="0 0 10 10"><path d="M9 5H2M5 1L1 5l4 4" stroke="#fff" stroke-width="2" fill="none"/></svg></span>
  <span class="n">1</span><span class="n">2</span><span class="n">3</span><span class="n">4</span><span class="n">5</span><span class="n">6</span><span class="n">7</span><span class="n">8</span><span class="n">9</span>
  <span class="arrow next"><svg width="10" height="10" viewBox="0 0 10 10"><path d="M1 5h7M5 1l4 4-4 4" stroke="#fff" stroke-width="2" fill="none"/></svg></span>
</div>

<aside class="filters abs">
  <div class="filter-head"><svg width="6" height="10"><path d="M0 0l6 5-6 5z" fill="#888"/></svg>Filter By Color</div>
  <ul class="colors">
    <li><span class="dot" style="background:#333"></span>Black</li>
    <li><span class="dot" style="background:#5b8ef0"></span>Blue</li>
    <li><span class="dot" style="background:#8a6150"></span>Brown</li>
    <li><span class="dot" style="background:#f3b21b"></span>Gold</li>
    <li><span class="dot" style="background:#7fd97c"></span>Green</li>
    <li><span class="dot" style="background:#ccc"></span>Grey</li>
    <li><span class="dot" style="background:#f5f3dc"></span>Ivory</li>
    <li><span class="dot" style="background:#fba466"></span>Orange</li>
    <li><span class="dot" style="background:#f8c4ea"></span>Pink</li>
    <li><span class="dot" style="background:#7a2378"></span>Purple</li>
    <li><span class="dot" style="background:#ee5a4c"></span>Red</li>
    <li><span class="dot" style="background:#f2f6fa"></span>Silver</li>
    <li><span class="dot" style="background:#fff"></span>White</li>
    <li><span class="dot" style="background:#fff27a"></span>Yellow</li>
    <li class="all">All Colors</li>
  </ul>
  <div class="filter-block" style="margin-top:8px"><div class="filter-head"><svg width="6" height="10"><path d="M0 0l6 5-6 5z" fill="#888"/></svg>Filter By Card Size</div></div>
  <div class="filter-block"><div class="filter-head"><svg width="6" height="10"><path d="M0 0l6 5-6 5z" fill="#888"/></svg>Filter By # of Photos</div></div>
  <div class="filter-block"><div class="filter-head"><svg width="6" height="10"><path d="M0 0l6 5-6 5z" fill="#888"/></svg>Filter By Designer</div></div>
</aside>

<div class="tile abs" style="left:391px;top:477px">
  <div class="art" role="img" aria-label="Pirate party invitation with parrot, pirate boy photo and ship" style="left:30px;top:0;width:161px;height:207px;background:linear-gradient(135deg,#2fa05a 0 25%,#d8272a 25% 50%,#f5a11c 50% 70%,#3b9bd6 70% 85%,#8cc63e 85%)"></div>
  <div class="quick">Quick View</div>
</div>
<div class="tile abs" style="left:619px;top:477px">
  <div class="art" role="img" aria-label="Birthday invitation with a toddler photo and colourful stars" style="left:30px;top:0;width:161px;height:207px;background:linear-gradient(#7fc242 0 48%,#1e9ad6 48% 62%,#f7a21b 62% 94%,#7fc242 94%)"></div>
  <div class="quick">Quick View</div>
</div>
<div class="tile abs" style="left:846px;top:477px;background:#fff">
  <div class="art" role="img" aria-label="Die-cut orange dinosaur birthday invitation" style="left:1px;top:1px;width:218px;height:128px;background:radial-gradient(ellipse at 55% 50%,#f7a21b 0 55%,#fff 56%)"></div>
  <div class="quick">Quick View</div>
</div>

<div class="tile abs" style="left:391px;top:704px">
  <div class="art" role="img" aria-label="Bowling strike birthday invitation with bowling ball and pins" style="left:61px;top:0;width:90px;height:207px;background:linear-gradient(#d8272a 0 18%,#3c9be0 18%)"></div>
  <div class="quick">Quick View</div>
</div>
<div class="tile abs" style="left:619px;top:704px">
  <div class="art" role="img" aria-label="Water slide birthday invitation with a boy sliding" style="left:1px;top:1px;width:218px;height:128px;background:linear-gradient(160deg,#a7d46a 0 45%,#f5c21c 45% 60%,#e9462e 60% 70%,#a7d46a 70%)"></div>
  <div class="quick">Quick View</div>
</div>
<div class="tile abs" style="left:846px;top:704px">
  <div class="art" role="img" aria-label="Space alien birthday invitation with flying saucer" style="left:1px;top:1px;width:218px;height:128px;background:radial-gradient(circle at 30% 45%,#7ed957 0 14%,#27a8e0 15%)"></div>
  <div class="quick">Quick View</div>
</div>

<div class="tile abs" style="left:391px;top:931px">
  <div class="art" role="img" aria-label="Yellow hang-out birthday invitation" style="left:30px;top:0;width:161px;height:40px;background:#f7d316"></div>
</div>
<div class="tile abs" style="left:619px;top:931px">
  <div class="art" role="img" aria-label="Cream birthday invitation with a red illustration" style="left:0;top:0;width:220px;height:40px;background:#f9e3a8"></div>
</div>
<div class="tile abs" style="left:846px;top:931px">
  <div class="art" role="img" aria-label="Green and orange birthday invitation" style="left:0;top:0;width:220px;height:40px;background:linear-gradient(90deg,#f39a1e 0 30%,#8cc63e 30%)"></div>
</div>

</body>
</html>
```